Velumin clinic business card - double sided for young clinic

I require business cards for my aesthetic clinic specialising in the below treatments. I would like the cards to be modern as my clinic base are young 22-35 years old. I require my logo on it and would like the edges to be rounded.

I have an aesthetic clinic specialising in :
Velumin
Lip Enhancement
Chemical Peels
Facial Fillers
Non Surgical Face Lift

I would the cards to have the following information on them:
My logo - (in grey/silver)
address
Phone number
services

Colours :
White/grey/silver and red

a nice image on there, perhaps a set of lips as this is a main service i deliver

Company Name: HFA Address: 52 Harwell Lane, 4 Brimfold High Street, TN7 4QW Phone: 0207 948 2176 Website: www.helenfosburyaesthetics-example.co.uk

Target Market(s)

clinics 22-45 years old mainly female

Industry/Entity Type

Business

Contact Information for Business Card

as above

Requirements
Must have
• logo
• Address
• Email
• Phone number
• Services i offer
Nice to have
• images

```html
<!DOCTYPE html>
<html lang="en">
<head>
<meta charset="utf-8">
<title>HFA business card</title>
<link rel="stylesheet" href="https://fonts.googleapis.com/css2?family=Didact+Gothic&family=Mulish:wght@800&family=Dancing+Script:wght@600&display=swap">
<style>
  :root {
    --bg: #141414;
    --card: #1f1f1f;
    --silver: #b8b8b8;
    --silver-soft: #a4a4a4;
    --ink: #151515;
  }
  * { box-sizing: border-box; margin: 0; padding: 0; }
  html, body { width: 1200px; height: 923px; overflow: hidden; background: var(--bg); }
  body { position: relative; font-family: "Didact Gothic", sans-serif; color: var(--silver); }

  .card {
    position: absolute; left: 290px; width: 620px; height: 400px;
    background: var(--card); border-radius: 26px;
  }
  .card--back { top: 40px; }
  .card--front { top: 483px; }

  /* back */
  .ornament-frame {
    position: absolute; left: 175px; top: 45px; width: 310px; height: 310px;
    border-radius: 50%; background: var(--silver-soft);
  }
  .services {
    position: absolute; left: 175px; top: 45px; width: 310px; height: 310px;
    display: flex; flex-direction: column; align-items: center; justify-content: center;
    font-family: "Dancing Script", cursive; font-weight: 600; color: var(--ink);
    font-size: 19px; line-height: 1.75; list-style: none; text-align: center;
  }
  .services__title { text-decoration: underline; font-size: 17px; }

  /* front */
  .brand {
    position: absolute; left: 30px; top: 105px; width: 220px;
    display: flex; flex-direction: column; align-items: center; text-align: center;
  }
  .brand__mark {
    width: 96px; height: 96px; border-radius: 50%; background: var(--silver-soft);
    display: flex; align-items: center; justify-content: center;
    color: var(--ink); font-size: 30px; letter-spacing: 2px;
  }
  .brand__name {
    margin-top: 14px; color: var(--silver); font-size: 20px;
    letter-spacing: 3px; line-height: 1.2; text-transform: uppercase;
  }
  .brand__name span { display: block; font-size: 27px; letter-spacing: 5px; }

  .divider {
    position: absolute; left: 262px; top: 70px; width: 1px; height: 270px;
    background: #4a4a4a;
  }

  .details { position: absolute; left: 282px; top: 72px; width: 328px; }
  .details__name { font-family: "Mulish", sans-serif; font-weight: 800; font-size: 19px; color: var(--silver); }
  .details__role { font-size: 16px; margin-top: 2px; }
  .details__address { font-style: normal; font-size: 16px; line-height: 1.45; margin-top: 22px; }
  .contact { list-style: none; margin-top: 26px; font-size: 14px; line-height: 1.9; }
  .contact li { display: flex; align-items: center; gap: 8px; white-space: nowrap; }
  .contact svg { width: 14px; height: 14px; flex: none; }
</style>
</head>
<body>

<section class="card card--back" aria-label="Card back">
  <div class="ornament-frame" role="img" aria-label="Scalloped lace frame ornament in silver grey"></div>
  <ul class="services">
    <li class="services__title">Specialising in:</li>
    <li>Velumin</li>
    <li>Lip Enhancement</li>
    <li>Non Surgical Face Lift</li>
    <li>Chemical Peels</li>
    <li>Facial Fillers</li>
  </ul>
</section>

<section class="card card--front" aria-label="Card front">
  <div class="brand">
    <div class="brand__mark">HFA</div>
    <p class="brand__name">Helen Fosbury <span>Aesthetics</span></p>
  </div>

  <div class="divider"></div>

  <div class="details">
    <p class="details__name">Helen Fosbury</p>
    <p class="details__role">Aesthetician</p>
    <address class="details__address">52 Harwell Lane<br>4 Brimfold High Street, TN7 4QW</address>
    <ul class="contact">
      <li>
        <svg viewBox="0 0 16 16" fill="none" stroke="currentColor" stroke-width="1.4"><path d="M4 2l2 3-1.5 1.5c.8 2 2.5 3.7 4.5 4.5L10.5 9.5l3 2-1.5 2.5C7 13.5 2.5 9 2 3.5z"/></svg>
        0207 948 2176
      </li>
      <li>
        <svg viewBox="0 0 16 16" fill="none" stroke="currentColor" stroke-width="1.4"><rect x="1.5" y="3.5" width="13" height="9"/><path d="M1.5 3.5L8 9l6.5-5.5"/></svg>
        hfabrimfoldbookings@example.com
      </li>
      <li>
        <svg viewBox="0 0 16 16" fill="none" stroke="currentColor" stroke-width="1.4"><circle cx="8" cy="8" r="6.5"/><ellipse cx="8" cy="8" rx="3" ry="6.5"/><path d="M1.5 8h13"/></svg>
        www.helenfosburyaesthetics-example.co.uk
      </li>
    </ul>
  </div>
</section>

</body>
</html>
```